Brightwire Hollow Business cards

one side I would like my logo (uploaded) and the other side I want my details. I'm an electrician in sydney. The logo side I'm happy with just a white background and our logo in the middle.

Details for other side
24/7 Sydney Electrician
Marcus Pell
0431 587 219
marcus@brightwirehollow.com.au
brightwirehollow.com.au
icons for facebook, instagram, linked in

Industry/Entity Type

electrician

Contact Information for Business Card

company info

```html
<!DOCTYPE html>
<html lang="en">
<head>
<meta charset="utf-8">
<title>Brightwire Hollow – Business Cards</title>
<link href="https://fonts.googleapis.com/css2?family=Michroma&family=Mulish:ital,wght@0,400;0,500;1,400;1,500&display=swap" rel="stylesheet">
<style>
  :root {
    --bg: #2b2b2b;
    --card-white: #ffffff;
    --brand-red: #ec3224;
    --ink: #111111;
    --on-red: #ffffff;
  }
  * { box-sizing: border-box; margin: 0; padding: 0; }
  html, body { width: 1200px; height: 875px; overflow: hidden; }
  body {
    background: var(--bg);
    display: flex;
    align-items: center;
    justify-content: center;
    gap: 36px;
    font-family: "Mulish", sans-serif;
  }
  .card {
    width: 560px;
    height: 320px;
    border-radius: 18px;
    position: relative;
    box-shadow: 0 18px 40px rgba(0,0,0,0.45);
  }
  /* Logo side */
  .card--front {
    background: var(--card-white);
    display: flex;
    align-items: center;
    justify-content: center;
    gap: 14px;
  }
  .brand-dot {
    width: 22px; height: 22px;
    border-radius: 50%;
    background: var(--brand-red);
  }
  .brand-name {
    font-family: "Michroma", sans-serif;
    font-size: 30px;
    color: var(--brand-red);
    text-transform: uppercase;
    letter-spacing: 1px;
    line-height: 1.15;
  }
  /* Details side */
  .card--back {
    background: var(--brand-red);
    color: var(--on-red);
  }
  .identity {
    position: absolute;
    left: 40px;
    top: 130px;
  }
  .identity__name {
    font-family: "Michroma", sans-serif;
    font-size: 24px;
    letter-spacing: 1px;
    text-transform: uppercase;
  }
  .identity__role {
    font-style: italic;
    font-size: 15px;
    margin-top: 4px;
    letter-spacing: 0.3px;
  }
  .divider {
    position: absolute;
    left: 300px;
    top: 62px;
    width: 14px;
    height: 120px;
  }
  .contacts {
    position: absolute;
    left: 326px;
    top: 72px;
    list-style: none;
    display: flex;
    flex-direction: column;
    gap: 9px;
    font-size: 12.5px;
    font-weight: 500;
  }
  .contacts li { display: flex; align-items: center; gap: 8px; white-space: nowrap; }
  .contacts svg { width: 13px; height: 13px; flex: none; }
  .contacts .phone { font-size: 15px; }
  .social {
    position: absolute;
    left: 330px;
    top: 220px;
    display: flex;
    gap: 8px;
  }
  .social__item {
    width: 24px; height: 24px;
    border-radius: 50%;
    background: var(--on-red);
  }
</style>
</head>
<body>
  <section class="card card--front" aria-label="Business card, logo side">
    <span class="brand-dot" aria-hidden="true"></span>
    <h1 class="brand-name">Brightwire<br>Hollow</h1>
  </section>

  <section class="card card--back" aria-label="Business card, details side">
    <div class="identity">
      <h2 class="identity__name">Marcus Pell</h2>
      <p class="identity__role">24/7 Sydney Electrician</p>
    </div>

    <svg class="divider" viewBox="0 0 14 120" aria-hidden="true">
      <rect x="4" y="0" width="1.6" height="7" fill="#fff"/>
      <rect x="8.4" y="0" width="1.6" height="7" fill="#fff"/>
      <rect x="2" y="6" width="10" height="9" rx="2" fill="#fff"/>
      <line x1="7" y1="15" x2="7" y2="120" stroke="#fff" stroke-width="1.4"/>
    </svg>

    <ul class="contacts">
      <li class="phone">
        <svg viewBox="0 0 24 24" aria-hidden="true"><path fill="#fff" d="M6.6 10.8a15.1 15.1 0 0 0 6.6 6.6l2.2-2.2a1 1 0 0 1 1-.25 11.4 11.4 0 0 0 3.6.57 1 1 0 0 1 1 1V20a1 1 0 0 1-1 1A17 17 0 0 1 3 4a1 1 0 0 1 1-1h3.5a1 1 0 0 1 1 1c0 1.25.2 2.45.57 3.57a1 1 0 0 1-.25 1z"/></svg>
        0431 587 219
      </li>
      <li>
        <svg viewBox="0 0 24 24" aria-hidden="true"><rect x="2" y="5" width="20" height="14" rx="1.5" fill="#fff"/><path d="M3 6l9 7 9-7" fill="none" stroke="#ec3224" stroke-width="1.8"/></svg>
        marcus@brightwirehollow.com.au
      </li>
      <li>
        <svg viewBox="0 0 24 24" aria-hidden="true"><circle cx="12" cy="12" r="9.5" fill="none" stroke="#fff" stroke-width="2"/><ellipse cx="12" cy="12" rx="4" ry="9.5" fill="none" stroke="#fff" stroke-width="1.6"/><line x1="2.5" y1="12" x2="21.5" y2="12" stroke="#fff" stroke-width="1.6"/></svg>
        brightwirehollow.com.au
      </li>
    </ul>

    <div class="social" aria-label="Social media profiles">
      <span class="social__item" aria-hidden="true"></span>
      <span class="social__item" aria-hidden="true"></span>
      <span class="social__item" aria-hidden="true"></span>
    </div>
  </section>
</body>
</html>
```